Residential Roofing Company

Website for Residential roofing company. Servicing Minnesota (Hennepin, Anoka, Sherburne County). Located in Ramsey, Minnesota. Asphalt Shingles (KLT and Darvell Pike Manufacturers)

Target Market(s)

Storm Damage repair. Roof Replacement and Repair.

Industry/Entity Type

Residential Roofing

Coding

Coded - Design and coding required

Number of Pages Required

5+ page

Colors

Designer to choose colors to be used in the design.

Requirements
Should not have
• No Commercial Roofing

```html
<!DOCTYPE html>
<html lang="en">
<head>
<meta charset="utf-8">
<title>Corvane Roofing</title>
<link href="https://fonts.googleapis.com/css2?family=Krona+One&family=Poppins:wght@400;500;600&display=swap" rel="stylesheet">
<style>
:root{
  --navy:#0b2c6c;
  --blue:#0b45a6;
  --blue-mid:#1060c0;
  --cyan:#19a8de;
  --light:#eef5fb;
  --text:#5a5f6b;
  --dark:#1e2433;
  --white:#ffffff;
}
*{box-sizing:border-box;margin:0;padding:0}
html,body{width:1200px;height:3655px;overflow:hidden}
body{position:relative;background:var(--white);font-family:"Poppins",sans-serif;color:var(--text)}
.abs{position:absolute}
.display{font-family:"Krona One",sans-serif;text-transform:uppercase}
.brand{font-family:"Poppins",sans-serif;font-weight:600;color:var(--blue);letter-spacing:1px;display:flex;align-items:center;gap:10px;white-space:nowrap}
.brand .mark{width:18px;height:18px;background:var(--blue)}
.nav{top:28px;left:568px;font-size:13.5px;color:var(--dark)}
.nav a{position:absolute;white-space:nowrap;text-decoration:none;color:var(--dark)}
.nav a.active{color:var(--blue)}
.call{left:1045px;top:16px;font-size:13px;color:var(--dark);line-height:22px}
.call b{font-weight:600}
.hero-photo{left:0;top:74px;width:1200px;height:560px;background:linear-gradient(180deg,#5f8fd0 0%,#8fb1dc 30%,#6c6e78 60%,#4a4f5c 100%)}
.hero-title{left:494px;top:222px;font-size:39px;line-height:46px;color:var(--white)}
.hero-text{left:494px;top:332px;width:630px;font-size:13.5px;line-height:22px;color:var(--white)}
.btn{display:flex;align-items:center;justify-content:center;color:var(--white);font-size:14px;background:linear-gradient(90deg,var(--blue),var(--cyan));clip-path:polygon(0 0,100% 0,97% 100%,4% 100%)}
.section-title{font-size:28px;line-height:41px;color:var(--blue);white-space:nowrap}
.welcome-text{left:61px;top:787px;width:525px;font-size:13.8px;line-height:22.5px}
.video{left:641px;top:715px;width:498px;height:320px;background:linear-gradient(135deg,#6c7584,#8e96a3 50%,#5d6573)}
.play{left:869px;top:855px;width:40px;height:40px;border-radius:50%;background:var(--cyan)}
.services-bg{left:0;top:1099px;width:1200px;height:568px;background:var(--light);clip-path:polygon(0 22px,100% 0,100% 100%,0 100%)}
.heading-row{display:flex;align-items:center;justify-content:center;gap:8px;width:1200px;left:0}
.heading-row .line{height:1.5px;width:70px;background:var(--dark)}
.heading-row.light .line{background:#6c8fd0}
.card{width:339px;height:386px;background:var(--white);box-shadow:0 2px 8px rgba(0,0,0,.08);top:1231px}
.card .img{width:339px;height:209px;position:relative}
.card .img svg{position:absolute;left:0;bottom:0}
.card h3{font-family:"Krona One",sans-serif;font-size:11.5px;color:var(--blue);margin:18px 15px 10px;text-transform:uppercase;letter-spacing:.3px}
.card p{font-size:13.5px;line-height:22.5px;margin:0 15px}
.card .more{position:absolute;left:15px;top:356px;font-size:13.5px;color:var(--cyan);display:flex;align-items:center;gap:6px}
.stat-num{font-family:"Krona One",sans-serif;font-size:28px;color:var(--white)}
.stat-label{font-size:13.5px;color:var(--white)}
.proj{background:var(--white);box-shadow:0 2px 10px rgba(0,0,0,.1);padding:9px}
.proj .img{width:100%}
.proj span{display:block;font-size:13.5px;color:var(--text);margin-top:10px}
.navy-bg{left:0;top:2458px;width:1200px;height:368px;background:var(--navy)}
.quote{font-size:13.5px;line-height:22.5px;color:var(--white);width:315px}
.avatar{width:72px;height:72px;border-radius:50%;background:linear-gradient(160deg,#f3e3d6,#d9b8a0);border:3px solid var(--white)}
.stars{display:flex;gap:4px}
.name{font-size:13.5px;color:var(--white)}
.arrow{width:38px;height:38px;border-radius:50%;display:flex;align-items:center;justify-content:center}
.quote-bg{left:0;top:2825px;width:1200px;height:508px;background:var(--light)}
.field{font-size:13.5px;color:var(--text);border-bottom:1.4px solid #7f8594;padding-left:3px}
.foot-h{font-family:"Krona One",sans-serif;font-size:12.5px;color:var(--blue);font-weight:400}
.foot-link{font-size:13.5px;color:var(--dark)}
.social{width:42px;height:32px;background:var(--blue)}
.copy{left:0;top:3624px;width:1200px;text-align:center;font-size:12px;color:var(--text)}
.copy b{color:var(--blue);font-weight:500}
</style>
</head>
<body>

<!-- Header -->
<header>
  <div class="abs brand" style="left:61px;top:22px;font-size:24px"><span class="mark"></span>CORVANE ROOFING</div>
  <nav class="abs nav">
    <a class="active" style="left:0">Home</a>
    <a style="left:80px">About</a>
    <a style="left:162px">Services</a>
    <a style="left:251px">Projects</a>
    <a style="left:338px">Contact</a>
  </nav>
  <svg class="abs" style="left:992px;top:17px" width="40" height="40" viewBox="0 0 40 40">
    <circle cx="20" cy="20" r="18" fill="none" stroke="#0b45a6" stroke-width="2.2"/>
    <path d="M13 12c1-1 2.5-1 3.2 0l1.8 2.6c.5.8.3 1.7-.4 2.3l-1.2 1c1 2 2.6 3.7 4.7 4.8l1-1.2c.6-.7 1.6-.9 2.3-.3l2.6 1.8c1 .7 1 2.2 0 3.1l-1.3 1.2c-1.3 1.1-3.2 1.2-4.7.4-4-2.2-7.2-5.5-9.4-9.5-.8-1.5-.6-3.3.5-4.5z" fill="#0b45a6"/>
    <path d="M22 11a7 7 0 0 1 7 7M22 14.5a3.5 3.5 0 0 1 3.5 3.5" stroke="#0b45a6" stroke-width="1.6" fill="none"/>
  </svg>
  <div class="abs call">Call Us<br><b>612-555-0147</b></div>
</header>

<!-- Hero -->
<section>
  <div class="abs hero-photo" role="img" aria-label="Photo of a house roof with dark asphalt shingles under a blue sky"></div>
  <svg class="abs" style="left:0;top:530px" width="1200" height="110" viewBox="0 530 1200 110">
    <defs><linearGradient id="heroBand" x1="0" x2="1"><stop offset="0" stop-color="#0a3f9e"/><stop offset=".6" stop-color="#0d5cc0"/><stop offset="1" stop-color="#1aa8de"/></linearGradient></defs>
    <polygon points="0,539 1200,610 1200,640 0,640" fill="#ffffff"/>
    <polygon points="0,539 1200,610 1200,634 0,617" fill="url(#heroBand)"/>
  </svg>
  <h1 class="abs display hero-title">Leaders in Quality<br>Roofing</h1>
  <p class="abs hero-text">Lorem Ipsum is simply dummy text of the printing and typesetting industry. Lorem Ipsum has been the industry's standard dummy text</p>
  <a class="abs btn" style="left:494px;top:418px;width:163px;height:36px">Contact Us Today</a>
</section>

<!-- Welcome -->
<section>
  <h2 class="abs display section-title" style="left:61px;top:700px">Welcome to Corvane<br>Roofing</h2>
  <p class="abs welcome-text">With over 40 years of experience in servicing the residents of the Twin Cities area, the Corvane Roofing team knows what it takes to get the job done right! We are a second generation roofing company that has instilled a modern touch into our brand. Corvane Roofing is a Woman Owned and Operated Company. We've implemented the knowledge and successful business practices from our history and experience into our brand. Roofing is our history and we strive to make sure our customers receive the best experience possible.</p>
  <a class="abs btn" style="left:61px;top:1000px;width:116px;height:36px">Read More</a>
  <div class="abs video" role="img" aria-label="Video still of roofers installing shingles on a steep roof"></div>
  <div class="abs play"><svg width="40" height="40" viewBox="0 0 40 40"><polygon points="16,13 28,20 16,27" fill="#fff"/></svg></div>
</section>

<!-- Services -->
<section>
  <div class="abs services-bg"></div>
  <div class="abs heading-row" style="top:1168px"><span class="line"></span><h2 class="display section-title">Our Services</h2><span class="line"></span></div>

  <article class="abs card" style="left:60px">
    <div class="img" role="img" aria-label="Photo of a two-storey house with a brown tiled roof" style="background:linear-gradient(180deg,#c9d4de 0%,#b07a55 45%,#8b5a3c 75%,#a9a27a 100%)">
      <svg width="339" height="26" viewBox="0 0 339 26"><polygon points="0,26 0,10 339,26" fill="#0b45a6"/></svg>
    </div>
    <h3>Residential Roofing</h3>
    <p>Corvane specializes in Residential roofing. With over 40 years of experience and 2 generations in the industry, we can assist you with the roofing system.</p>
    <a class="more">Read More <svg width="26" height="10" viewBox="0 0 26 10"><path d="M0 5h24M19 1l5 4-5 4" stroke="#19a8de" stroke-width="1.4" fill="none"/></svg></a>
  </article>

  <article class="abs card" style="left:431px">
    <div class="img" role="img" aria-label="Photo of a storm-damaged shingle roof under grey clouds" style="background:linear-gradient(180deg,#6f7a86 0%,#9aa3ad 18%,#4c5560 40%,#2f363e 100%)">
      <svg width="339" height="26" viewBox="0 0 339 26"><polygon points="0,26 0,10 339,26" fill="#0b45a6"/></svg>
    </div>
    <h3>Storm Damage Repair</h3>
    <p>Hail and high winds take a toll on any roof. We inspect, document the damage and work with your insurance to restore your home fast.</p>
    <a class="more">Read More <svg width="26" height="10" viewBox="0 0 26 10"><path d="M0 5h24M19 1l5 4-5 4" stroke="#19a8de" stroke-width="1.4" fill="none"/></svg></a>
  </article>

  <article class="abs card" style="left:800px">
    <div class="img" role="img" aria-label="Photo of a large house with cream siding and windows" style="background:linear-gradient(180deg,#9aaec4 0%,#cfd3d6 30%,#d8d2c2 60%,#6f8a4e 100%)">
      <svg width="339" height="26" viewBox="0 0 339 26"><polygon points="0,26 0,10 339,26" fill="#0b45a6"/></svg>
    </div>
    <h3>Siding / Windows</h3>
    <p>Whether you need new siding installed or if you need help with your insurance claim after a damaging storm. Our dedicated project managers will see</p>
    <a class="more">Read More <svg width="26" height="10" viewBox="0 0 26 10"><path d="M0 5h24M19 1l5 4-5 4" stroke="#19a8de" stroke-width="1.4" fill="none"/></svg></a>
  </article>
</section>

<!-- Stats -->
<section>
  <svg class="abs" style="left:0;top:1667px" width="1200" height="208" viewBox="0 1667 1200 208">
    <defs><linearGradient id="statBand" x1="0" x2="1"><stop offset="0" stop-color="#0a3d9c"/><stop offset=".5" stop-color="#0b5dbf"/><stop offset="1" stop-color="#1ab0e2"/></linearGradient></defs>
    <polygon points="0,1667 1200,1763 0,1875" fill="url(#statBand)"/>
  </svg>
  <div class="abs stat-num" style="left:71px;top:1732px">1987</div>
  <div class="abs stat-label" style="left:61px;top:1780px">Year Established</div>
  <div class="abs stat-num" style="left:340px;top:1732px">1000's</div>
  <div class="abs stat-label" style="left:337px;top:1780px">Satisfied Customers</div>
</section>

<!-- Projects -->
<section>
  <div class="abs heading-row" style="top:1910px"><span class="line"></span><h2 class="display section-title">Our Projects</h2><span class="line"></span></div>
  <div class="abs proj" style="left:92px;top:2031px;width:139px;height:245px">
    <div class="img" style="height:196px;background:linear-gradient(135deg,#c9d6e2,#c49a7c 50%,#a7765a)" role="img" aria-label="Photo of a house gable with white trim"></div>
    <span>Project Name</span>
  </div>
  <div class="abs proj" style="left:231px;top:2007px;width:142px;height:293px">
    <div class="img" style="height:235px;background:linear-gradient(180deg,#d6dee6,#6f7880 35%,#565d64)" role="img" aria-label="Photo of a metal standing seam roof"></div>
    <span>Project Name</span>
  </div>
  <div class="abs proj" style="left:827px;top:2007px;width:145px;height:293px">
    <div class="img" style="height:235px;background:linear-gradient(160deg,#3f4654,#6c5a48 55%,#a36c3a)" role="img" aria-label="Photo of a roof being stripped down to the decking"></div>
  </div>
  <div class="abs proj" style="left:972px;top:2031px;width:136px;height:245px">
    <div class="img" style="height:196px;background:linear-gradient(180deg,#dde6ee,#6d7177 30%,#555a60)" role="img" aria-label="Photo of a shingled roof with trees behind"></div>
  </div>
  <div class="abs proj" style="left:372px;top:1970px;width:455px;height:359px">
    <div class="img" style="height:290px;background:linear-gradient(160deg,#4f7a3a,#7ea25a 40%,#8a6a52 55%,#6f9a4c)" role="img" aria-label="Aerial photo of a house with a brown roof and a backyard pool"></div>
    <span>Project Name</span>
  </div>
</section>

<!-- Testimonials -->
<section>
  <svg class="abs" style="left:0;top:2380px" width="1200" height="110" viewBox="0 2380 1200 110">
    <defs><linearGradient id="testBand" x1="0" x2="1"><stop offset="0" stop-color="#0a3e9e"/><stop offset=".7" stop-color="#0b5ec0"/><stop offset="1" stop-color="#1aa8de"/></linearGradient></defs>
    <polygon points="0,2383 1200,2475 1200,2482 0,2460" fill="url(#testBand)"/>
  </svg>
  <div class="abs navy-bg"></div>
  <div class="abs heading-row light" style="top:2522px"><span class="line"></span><h2 class="display section-title" style="color:#fff">What are our client says</h2><span class="line"></span></div>

  <div class="abs arrow" style="left:39px;top:2645px;background:#fff"><svg width="14" height="14" viewBox="0 0 14 14"><path d="M9 2L4 7l5 5" stroke="#0b2c6c" stroke-width="1.6" fill="none"/></svg></div>
  <div class="abs arrow" style="left:1120px;top:2645px;background:var(--cyan)"><svg width="14" height="14" viewBox="0 0 14 14"><path d="M5 2l5 5-5 5" stroke="#fff" stroke-width="1.6" fill="none"/></svg></div>

  <div class="abs avatar" style="left:167px;top:2589px" role="img" aria-label="Client portrait"></div>
  <p class="abs quote" style="left:259px;top:2586px">Lorem Ipsum is simply dummy text of the printing and typesetting industry. Lorem Ipsum has been the industry's standard dummy text ever since the 1500s, when an unknown printer took a galley of type...</p>
  <div class="abs stars" style="left:261px;top:2715px">
    <svg width="100" height="18" viewBox="0 0 100 18"><g fill="#f6d200"><polygon id="st" points="9,0 11.6,6 18,6.5 13,10.8 14.6,17 9,13.6 3.4,17 5,10.8 0,6.5 6.4,6"/><use href="#st" x="20"/><use href="#st" x="40"/><use href="#st" x="60"/><use href="#st" x="80"/></g></svg>
  </div>
  <div class="abs name" style="left:261px;top:2746px">Mara Ellison</div>

  <div class="abs avatar" style="left:615px;top:2589px" role="img" aria-label="Client portrait"></div>
  <p class="abs quote" style="left:708px;top:2586px">Lorem Ipsum is simply dummy text of the printing and typesetting industry. Lorem Ipsum has been the industry's standard dummy text ever since the 1500s, when an unknown printer took a galley of type...</p>
  <div class="abs stars" style="left:710px;top:2715px">
    <svg width="100" height="18" viewBox="0 0 100 18"><g fill="#f6d200"><use href="#st"/><use href="#st" x="20"/><use href="#st" x="40"/><use href="#st" x="60"/><use href="#st" x="80"/></g></svg>
  </div>
  <div class="abs name" style="left:710px;top:2746px">Mara Ellison</div>
</section>

<!-- Quote form -->
<section>
  <div class="abs quote-bg"></div>
  <div class="abs" style="left:460px;top:2880px;width:603px;display:flex;align-items:center;gap:6px">
    <span style="flex:1;height:1.5px;background:var(--dark)"></span>
    <h2 class="display section-title">Geat a Free Quote</h2>
    <span style="flex:1;height:1.5px;background:var(--dark)"></span>
  </div>
  <div class="abs field" style="left:460px;top:2940px;width:322px;height:26px">First Name*</div>
  <div class="abs field" style="left:813px;top:2940px;width:322px;height:26px">Last Name*</div>
  <div class="abs field" style="left:460px;top:2992px;width:322px;height:27px">E-mail*</div>
  <div class="abs field" style="left:813px;top:2992px;width:322px;height:27px">Subject*</div>
  <div class="abs field" style="left:460px;top:3040px;width:675px;height:126px">Massage*</div>
  <a class="abs btn" style="left:740px;top:3233px;width:93px;height:35px">Submit</a>
</section>

<!-- Footer -->
<footer>
  <div class="abs brand" style="left:61px;top:3410px;font-size:22px"><span class="mark"></span>CORVANE ROOFING</div>
  <p class="abs" style="left:61px;top:3483px;width:240px;font-size:13.5px;line-height:22.5px">With over 40 years of experience in servicing the residents of the Twin Cities area, the Corvane Roofing team</p>

  <h4 class="abs foot-h" style="left:337px;top:3384px">SITE MAP</h4>
  <div class="abs foot-link" style="left:337px;top:3414px">Home</div>
  <div class="abs foot-link" style="left:337px;top:3451px">About</div>
  <div class="abs foot-link" style="left:337px;top:3487px">Services</div>
  <div class="abs foot-link" style="left:337px;top:3523px">Projects</div>
  <div class="abs foot-link" style="left:337px;top:3560px">Contact</div>

  <h4 class="abs foot-h" style="left:613px;top:3384px">CONTACT US</h4>
  <svg class="abs" style="left:611px;top:3416px" width="16" height="20" viewBox="0 0 16 20"><path d="M8 1a6 6 0 0 1 6 6c0 4.5-6 11-6 11S2 11.5 2 7a6 6 0 0 1 6-6z" fill="none" stroke="#0b45a6" stroke-width="1.6"/><circle cx="8" cy="7" r="2.2" fill="#19a8de"/></svg>
  <div class="abs foot-link" style="left:640px;top:3417px">Alder Falls, MN 55399</div>
  <svg class="abs" style="left:611px;top:3458px" width="18" height="18" viewBox="0 0 18 18"><path d="M3 3c.8-.8 2-.8 2.6 0l1.4 2c.4.6.3 1.4-.3 1.8l-.9.8c.8 1.6 2.1 2.9 3.7 3.7l.8-.9c.5-.6 1.3-.7 1.8-.3l2 1.4c.8.6.8 1.8 0 2.5l-1 1c-1 .9-2.5 1-3.7.3C6.3 13.6 4.4 11.7 3 9.1c-.7-1.2-.5-2.7.4-3.6z" fill="#0b45a6"/></svg>
  <div class="abs foot-link" style="left:640px;top:3458px;font-weight:500">612-555-0147</div>
  <svg class="abs" style="left:611px;top:3497px" width="18" height="13" viewBox="0 0 18 13"><rect x=".8" y=".8" width="16.4" height="11.4" fill="none" stroke="#0b45a6" stroke-width="1.5"/><path d="M1 1l8 6 8-6" fill="none" stroke="#0b45a6" stroke-width="1.5"/></svg>
  <div class="abs foot-link" style="left:640px;top:3493px">Office@corvaneroofing.com</div>

  <h4 class="abs foot-h" style="left:891px;top:3384px">STAY IN TOUCH</h4>
  <div class="abs social" style="left:891px;top:3424px" aria-label="Social profile"></div>
  <div class="abs social" style="left:943px;top:3424px;background:var(--cyan)" aria-label="Social profile"></div>

  <div class="abs" style="left:0;top:3613px;width:1200px;height:1px;background:#c8ccd4"></div>
  <div class="abs copy">© Copyright 2022 <b>CORVANE ROOFING</b>.All Right Reserved.</div>
</footer>

</body>
</html>
```